New Business Card for Software Company

We are looking at rebranding a 10 year old company that specializes in PDF and DWF solutions for Architects and Engineers. We will attach the new company logo that we are going with so you can work with that and complimentary colors.
The sample information we would like on the business card is:
Gerald Pembrook
Vice President
4173 W. Tillman Avenue. STE 306
PMB#417
Corvel, NV 85316
866-392-7154 US Toll Free
123-581-3064 Cell
gpembrook@vextrolan.com
The old tag line that we had on the business cars was.
Delivering Dependable Document and Drawing Tools to Design Teams Everywhere.
If you have an idea for a better tag line we are open to that also.
Updates
We would like to thank all of the Designers for their wonderful work. We apologize that we will not have the time to provide feedback to everyone. There is just so many innovative and professional designs that you have all created making our decision even harder.
Target Market(s)
Architects and Engineers
Industry/Entity Type
Business
Look and feel
Each slider illustrates characteristics of the customer's brand and the style your logo design should communicate.

```html
<!DOCTYPE html>
<html lang="en">
<head>
<meta charset="utf-8">
<title>Vextrolan Business Card</title>
<link href="https://fonts.googleapis.com/css2?family=Open+Sans:ital,wght@0,400;0,600;0,700;0,800;1,600;1,700&display=swap" rel="stylesheet">
<style>
  :root {
    --bg: #e9e7e6;
    --card-white: #ffffff;
    --charcoal: #544b49;
    --ink-grey: #6f6a69;
    --accent: #ec3e16;
    --accent-warm: #f7821f;
    --shadow: rgba(40, 30, 28, 0.22);
  }
  * { margin: 0; padding: 0; box-sizing: border-box; }
  html, body {
    width: 1200px; height: 900px; overflow: hidden;
    background: var(--bg);
    font-family: "Open Sans", Arial, sans-serif;
  }
  .stage { position: relative; width: 1200px; height: 900px; }
  .card {
    position: absolute; left: 280px; width: 640px; height: 366px;
    border-radius: 18px; overflow: hidden;
    background: var(--card-white);
    box-shadow: 0 10px 28px var(--shadow);
  }
  .card-back { top: 52px; }
  .card-front { top: 482px; }
  .card-art { position: absolute; inset: 0; width: 100%; height: 100%; }

  /* Back */
  .tagline {
    position: absolute; left: 62px; top: 92px; width: 480px;
    color: #fff; font-style: italic; font-weight: 700;
    font-size: 19px; line-height: 1.25;
  }
  .back-brand {
    position: absolute; right: 38px; top: 262px;
    font-weight: 800; font-size: 38px; letter-spacing: -1px;
    color: var(--accent);
  }

  /* Front */
  .front-brand {
    position: absolute; left: 40px; top: 34px;
    display: flex; align-items: center; gap: 10px;
  }
  .brand-dot { width: 40px; height: 40px; border-radius: 50%; background: var(--accent); }
  .brand-name { font-weight: 800; font-size: 38px; letter-spacing: -1px; color: var(--accent); }
  .address {
    position: absolute; left: 48px; top: 112px;
    color: var(--ink-grey); font-size: 15px; line-height: 1.35;
  }
  .contact {
    position: absolute; left: 48px; top: 178px;
    font-size: 15px; line-height: 1.4; color: var(--ink-grey);
  }
  .contact .label { color: var(--accent); font-weight: 600; }
  .contact .web { color: var(--accent); font-weight: 600; }
  .person { position: absolute; right: 48px; top: 236px; text-align: right; }
  .person-name { color: var(--accent); font-weight: 600; font-size: 22px; }
  .person-title { color: var(--ink-grey); font-size: 15px; }
</style>
</head>
<body>
<main class="stage">

  <section class="card card-back">
    <svg class="card-art" viewBox="0 0 640 366" preserveAspectRatio="none">
      <defs>
        <linearGradient id="glow" x1="0" y1="0" x2="1" y2="1">
          <stop offset="0" stop-color="#f08a2a" stop-opacity="0.55"/>
          <stop offset="1" stop-color="#d8461e" stop-opacity="0.35"/>
        </linearGradient>
      </defs>
      <rect width="640" height="366" fill="var(--card-white)"/>
      <path d="M0 0 H640 V198 H470 C430 198 418 240 370 246 H0 Z" fill="var(--charcoal)"/>
      <rect x="30" y="0" width="210" height="246" rx="60" fill="url(#glow)" role="img" aria-label="Soft orange decorative glow"/>
      <rect x="0" y="350" width="640" height="16" fill="var(--accent)"/>
    </svg>
    <p class="tagline">Delivering Dependable Document and Drawing Tools to Design Teams Everywhere</p>
    <div class="back-brand">Vextrolan</div>
  </section>

  <section class="card card-front">
    <svg class="card-art" viewBox="0 0 640 366" preserveAspectRatio="none">
      <defs>
        <linearGradient id="swoosh" x1="0" y1="0" x2="1" y2="0">
          <stop offset="0" stop-color="var(--accent-warm)"/>
          <stop offset="1" stop-color="var(--accent)"/>
        </linearGradient>
      </defs>
      <rect width="640" height="366" fill="var(--card-white)"/>
      <path d="M330 366 C345 346 350 336 372 336 H640 V366 Z" fill="url(#swoosh)"/>
      <rect x="0" y="360" width="330" height="6" fill="var(--charcoal)"/>
    </svg>
    <div class="front-brand">
      <span class="brand-dot"></span>
      <span class="brand-name">Vextrolan</span>
    </div>
    <p class="address">4173 W. Tillman Avenue. STE 306<br>PMB#417 Corvel, NV 85316</p>
    <p class="contact">
      <span class="label">Toll Free.</span> 866-392-7154<br>
      <span class="label">Cell.</span> 123-581-3064<br>
      <span class="label">Email.</span> gpembrook@vextrolan.com<br>
      <span class="web">www.vextrolan.com</span>
    </p>
    <div class="person">
      <div class="person-name">Gerald Pembrook</div>
      <div class="person-title">Vice President</div>
    </div>
  </section>

</main>
</body>
</html>
```